Postcard Design

Bramble Circuit Holdings is a waste and Recycling company. We want to purchase recyclable materials from businesses. We would like to use the colors green and grey. The exact colors needed in this project are described below. We would like to have a picture of waste cardboard,a picture of money, and and the line- Are you getting top dollar for your Recyclables? After please put our logo and our phone number: 800.472.5196, our website (tindlepath.com),
and our email address: marguerite@tindlepath.com.

* Postcard must contain our logo. Please see buisness card for branding

Industry/Entity Type

It Company

Requirements
Must have
• This postcard must contain the logo and these colors:
Pantone: 576C & 418C

```html
<!DOCTYPE html>
<html lang="en">
<head>
<meta charset="utf-8">
<title>Bramble Circuit Holdings – Postcard</title>
<link href="https://fonts.googleapis.com/css2?family=Roboto+Condensed:wght@700&family=Open+Sans:wght@700&display=swap" rel="stylesheet">
<style>
  :root {
    --green: #5d8a3a;
    --green-dark: #4f7a30;
    --grey: #5e5f58;
    --grey-light: #b9b9b6;
    --paper: #ffffff;
    --cardboard-a: #b59a72;
    --cardboard-b: #8f7a5c;
    --bill-a: #e4e6d6;
    --bill-b: #c9cfb8;
  }
  * { margin: 0; padding: 0; box-sizing: border-box; }
  html, body { width: 1200px; height: 464px; overflow: hidden; background: var(--paper); }
  .canvas { position: relative; width: 1200px; height: 464px; background: var(--paper); }

  /* Front side */
  .front { position: absolute; left: 0; top: 0; width: 600px; height: 464px; }
  .front__backdrop { position: absolute; left: 0; top: 0; width: 600px; height: 200px;
    background: linear-gradient(180deg, #9c9d99 0%, #b3b4b0 100%); }
  .photo-cardboard { position: absolute; left: 0; top: 0; width: 305px; height: 200px;
    background: linear-gradient(135deg, var(--cardboard-a) 0%, var(--cardboard-b) 60%, #a58d68 100%); }
  .photo-bill { position: absolute; left: 300px; top: 2px; width: 262px; height: 136px;
    background: linear-gradient(160deg, var(--bill-a) 0%, var(--bill-b) 100%);
    transform: rotate(-1deg); }
  .front__mist { position: absolute; left: 0; top: 150px; width: 600px; height: 50px;
    background: rgba(236, 236, 232, 0.78); }
  .front__band { position: absolute; left: 0; top: 200px; width: 600px; height: 125px; background: var(--green); }

  .headline { position: absolute; left: 0; top: 0; width: 600px;
    font-family: "Roboto Condensed", "Arial Narrow", sans-serif; font-weight: 700; line-height: 1; }
  .headline span { position: absolute; white-space: nowrap; letter-spacing: 0.3px;
    transform: scaleX(1.16); transform-origin: left top; }
  .headline__lead { left: 47px; top: 150px; font-size: 45px; color: var(--green); }
  .headline__main { left: 84px; top: 206px; font-size: 60px; color: var(--paper); }
  .headline__tail { left: 20px; top: 266px; font-size: 52px; color: var(--paper); }

  .brand { position: absolute; display: flex; align-items: center; gap: 8px; white-space: nowrap;
    font-family: "Open Sans", Arial, sans-serif; font-weight: 700; color: var(--grey); }
  .brand__mark { width: 14px; height: 14px; background: var(--green); flex: none; }
  .brand--front { left: 40px; top: 392px; font-size: 16px; }
  .brand--back { left: 626px; top: 70px; font-size: 14px; }

  .contact { position: absolute; text-align: center; font-style: normal;
    font-family: "Open Sans", Arial, sans-serif; font-weight: 700; }
  .contact__phone, .contact__email { color: var(--green); }
  .contact__web { color: var(--grey); }
  .contact--front { left: 282px; top: 355px; width: 290px; font-size: 19px; line-height: 27px; }
  .contact--back { left: 832px; top: 47px; width: 210px; font-size: 13.5px; line-height: 20px; }

  /* Back side */
  .back { position: absolute; left: 600px; top: 0; width: 600px; height: 464px; }
  .back__topbar { position: absolute; left: 0; top: 0; width: 450px; height: 15px; background: var(--green); }
  .back__sidebar { position: absolute; left: 0; top: 0; width: 15px; height: 148px; background: var(--green-dark); }
  .back__fold { position: absolute; left: 0; top: 148px; width: 1px; height: 316px;
    border-left: 1px dashed var(--grey-light); }
</style>
</head>
<body>
<main class="canvas">
  <section class="front">
    <div class="front__backdrop"></div>
    <div class="photo-cardboard" role="img" aria-label="Photo of stacked bales of waste cardboard"></div>
    <div class="photo-bill" role="img" aria-label="Photo of a one-dollar bill"></div>
    <div class="front__mist"></div>
    <div class="front__band"></div>
    <h1 class="headline">
      <span class="headline__lead">Are you getting</span>
      <span class="headline__main">top dollar</span>
      <span class="headline__tail">for your Recyclables?</span>
    </h1>
    <div class="brand brand--front"><span class="brand__mark"></span>Bramble Circuit Holdings</div>
    <address class="contact contact--front">
      <div class="contact__phone">800.472.5196</div>
      <div class="contact__web">www.tindlepath.com</div>
      <div class="contact__email">marguerite@tindlepath.com</div>
    </address>
  </section>

  <section class="back">
    <div class="back__topbar"></div>
    <div class="back__sidebar"></div>
    <div class="back__fold"></div>
  </section>
  <div class="brand brand--back"><span class="brand__mark"></span>Bramble Circuit Holdings</div>
  <address class="contact contact--back">
    <div class="contact__phone">800.472.5196</div>
    <div class="contact__web">www.tindlepath.com</div>
    <div class="contact__email">marguerite@tindlepath.com</div>
  </address>
</main>
</body>
</html>
```